Meadow Lantern Veterinary Practice including Nest2Grow

We require a double-sided full colour tri-fold Brochure for Print.
Colour theme to in line with logo below

Written CONTENT below
Orphans
We can provide care and a new mother for orphan foals of any age, breed or size, from thoroughbreds and draft breeds to tiny ponies and even donkeys.
We have successfully fostered orphans from a few hours of age through to eight weeks, regardless of how long or if at all they were with their birth mother, and of previous fostering attempts.
We have the knowledge and experience to provide optimum nutrition and care to orphans during the brief period that they don’t have a mum, until their new foster mother is ready to take them.
Additionally we are a veterinary practice, and can provide diagnostics and therapeutics for compromised orphan foals such as plasma administration and health checks.

Mares
Nest2Grow mares have been selected for mothering ability and temperament, and have all carried and raised at least one foal of their own. Many have already been successful foster mothers in one or more of the last five breeding seasons.
The mares are not currently pregnant and are given a carefully designed course of hormones to induce lactation when required. The milk produced is not colostrum, but is completely normal and equivalent to that which they would have had if the foal was theirs by birth.
There is published scientific information (in addition to our own experience and that of the owners of previous graduates of our programme) that growth and development of foals raised by induced lactation is identical to that of foals raised by their birth mothers.

Fostering
During the few days when the mare’s udder is developing, mare and foal are kept next separately but in close proximity, allowing bonding to begin and reducing stress on the orphan.
The fostering is completed once the mare has enough milk to feed the foal, and our experienced handlers ensure that joining the two goes smoothly.
Once they are together the mare completely accepts the foal as her own, and the foal can suckle freely – at this stage we continue to offer supplementary feeds until they are not needed.
The mare and foal are then a normal unit and can return to the foal owner’s care until weaning – ensuring optimum nutrition and behaviour for the foal and excellent outcomes in performance, relationships with other horses, and interaction with humans.

Complete Safety
Mares recognise their birth foal by scent - a unique bond established during the first few minutes of the foal’s life - and only a small percentage of mares who have lost their own foal will readily accept a substitute.
When a mare who has lost her birth foal is offered an orphan, it is very normal and common for her to respond with aggression - to the danger of the foal and the human handler.
Nest2Grow mares have no birth foal in the current season, and are happy to adopt any foal who is placed close to them during the hormone treatment period.
This makes for total foal and handler safety.

Excellent Success Rate
After seven years of perfecting the fostering method, Nest2Grow can claim total success: we have now documented almost 50 fosterings over the last five breeding seasons. We have never been entrusted with an orphan foal that we have not been able to provide with a beautiful foster mum.

Career Mothers
Being dedicated career mothers with no other job in life, our mares are free to accompany their new foals home and stay with them as long as required. No foals are weaned and left without a mother in our programme, and our beautiful mares who would otherwise not be bred, are given a foal every year and a wonderful lifelong purpose.

Every single orphan’s human family has admired and appreciated our beautiful mares, with many offering to give them a home for life. Each season as the orphans are weaned, we welcome our mares home to Meadow Lantern to prepare for the next foal in need – a job they totally love! – just as if they were in a natural breeding situation.

Meadow Lantern Vet Practice including Nest2Grow
214 Pellerby Lane
Thornvale. Vic. 3812

Phone 0431958617 or 0419284056

```html
<!DOCTYPE html>
<html lang="en">
<head>
<meta charset="utf-8">
<title>Nest2Grow Brochure – Inside Spread</title>
<link rel="stylesheet" href="https://fonts.googleapis.com/css2?family=Quicksand:wght@400;500;600;700&display=swap">
<style>
  :root {
    --canvas: #ecebe8;
    --paper: #f8f7f4;
    --paper-shade: #efeeea;
    --ink: #4a4a4a;
    --accent: #e9822b;
    --photo-dark: #4b3a30;
    --photo-mid: #6f7a55;
    --photo-light: #b9b3a4;
    --bottle: #f3d9d2;
  }
  * { box-sizing: border-box; margin: 0; padding: 0; }
  html, body {
    width: 1200px; height: 800px; overflow: hidden;
    background: var(--canvas);
    font-family: "Quicksand", sans-serif;
    color: var(--ink);
  }
  .spread {
    position: absolute; left: 70px; top: 40px;
    width: 1060px; height: 720px;
    display: flex;
  }
  .page {
    position: relative;
    width: 530px; height: 720px;
    overflow: hidden;
    display: flex; flex-direction: column;
    padding: 50px 52px 30px 56px;
  }
  .page--left {
    background: linear-gradient(to right, var(--paper) 82%, var(--paper-shade));
  }
  .page--right {
    background: linear-gradient(to right, var(--paper-shade), var(--paper) 12%);
    padding-left: 48px; padding-right: 56px;
  }
  .section { margin-bottom: 24px; }
  .section__title {
    display: inline-block;
    font-size: 17px; font-weight: 600;
    color: var(--accent);
    border-bottom: 2px dashed var(--accent);
    padding-bottom: 1px;
    margin-bottom: 7px;
  }
  .section p {
    font-size: 12px; line-height: 1.4;
    font-weight: 500;
  }
  .photo-row {
    display: flex; align-items: flex-end; gap: 14px;
    margin-top: auto;
  }
  .photo {
    width: 170px; height: 132px;
    border-radius: 48% 52% 46% 54% / 55% 50% 50% 45%;
    flex: none;
  }
  .photo--mare-handler {
    background: radial-gradient(circle at 45% 55%, var(--photo-dark) 0%, #5d4637 45%, var(--photo-light) 100%);
  }
  .photo--foal-family {
    background: radial-gradient(circle at 50% 50%, var(--photo-dark) 0%, var(--photo-mid) 60%, #8e9a74 100%);
    margin-bottom: 24px;
  }
  .bottle {
    width: 34px; height: 54px;
    align-self: flex-start;
    margin-left: 8px;
    transform: rotate(-28deg);
    flex: none;
  }
</style>
</head>
<body>
  <main class="spread">
    <section class="page page--left">
      <article class="section">
        <h2 class="section__title">Orphans</h2>
        <p>We can provide care and a new mother for orphan foals of any age, breed or size, from thoroughbreds and draft breeds to tiny ponies and even donkeys.</p>
        <p>We have successfully fostered orphans from a few hours of age through to eight weeks, regardless of how long or if at all they were with their birth mother, and of previous fostering attempts.</p>
        <p>We have the knowledge and experience to provide optimum nutrition and care to orphans during the brief period that they don’t have a mum, until their new foster mother is ready to take them.</p>
        <p>Additionally we are a veterinary practice, and can provide diagnostics and therapeutics for compromised orphan foals such as plasma administration and health checks.</p>
      </article>
      <article class="section">
        <h2 class="section__title">Mares</h2>
        <p>Nest2Grow mares have been selected for mothering ability and temperament, and have all carried and raised at least one foal of their own. Many have already been successful foster mothers in one or more of the last five breeding seasons.</p>
        <p>The mares are not currently pregnant, and are given a carefully designed course of hormones to induce lactation when required. The milk produced is not colostrum, but is completely normal and equivalent to that which they would have had if the foal was theirs by birth.</p>
        <p>There is published scientific information (in addition to our own experience and that of the owners of previous graduates of our programme) that growth and development of foals raised by induced lactation is identical to that of foals raised by their birth mothers.</p>
      </article>
      <div class="photo-row">
        <div class="photo photo--mare-handler" role="img" aria-label="Photo of a bay mare and her foal with a handler beside a fence"></div>
        <div class="photo photo--foal-family" role="img" aria-label="Photo of a woman standing with a mare and two foals in a paddock"></div>
        <svg class="bottle" viewBox="0 0 34 54" role="img" aria-label="Illustration of a baby bottle">
          <rect x="3" y="12" width="28" height="40" rx="7" fill="var(--bottle)"/>
        </svg>
      </div>
    </section>

    <section class="page page--right">
      <article class="section">
        <h2 class="section__title">Fostering</h2>
        <p>During the few days when the mare’s udder is developing, mare and foal are kept next separately but in close proximity, allowing bonding to begin and reducing stress on the orphan.</p>
        <p>The fostering is completed once the mare has enough milk to feed the foal, and our experienced handlers ensure that joining the two goes smoothly.</p>
        <p>Once they are together the mare completely accepts the foal as her own, and the foal can suckle freely – at this stage we continue to offer supplementary feeds until they are not needed.</p>
        <p>The mare and foal are then a normal unit and can return to the foal owner’s care until weaning – ensuring optimum nutrition and behaviour for the foal and excellent outcomes in performance, relationships with other horses, and interaction with humans.</p>
      </article>
      <article class="section">
        <h2 class="section__title">Complete Safety</h2>
        <p>Mares recognise their birth foal by scent - a unique bond established during the first few minutes of the foal’s life - and only a small percentage of mares who have lost their own foal will readily accept a substitute.</p>
        <p>When a mare who has lost her birth foal is offered an orphan, it is very normal and common for her to respond with aggression - to the danger of the foal and the human handler.</p>
        <p>Nest2Grow mares have no birth foal in the current season, and are happy to adopt any foal who is placed close to them during the hormone treatment period.</p>
        <p>This makes for total foal and handler safety.</p>
      </article>
      <article class="section">
        <h2 class="section__title">Excellent Success Rate</h2>
        <p>After seven years of perfecting the fostering method, Nest2Grow can claim total success: we have now documented almost 50 fosterings over the last five breeding seasons. We have never been entrusted with an orphan foal that we have not been able to provide with a beautiful foster mum.</p>
      </article>
    </section>
  </main>
</body>
</html>
```